Coffee Bag Label

I need a coffee bag label designed (front label and back label):
Our company "Tidy-Pod" imports organic coffee beans direct from a farm on Vorsela Mountain on a private reserve (rainforest) from Jinotega, Nicaragua.
Labels should each be 3 inches x 3 inches (with room on edges for bleed). I want the front label to catch the eye and coordinate well with the coffee bag. The bags sizes are below and pictures are attached.
Bag sizes: Lime green 12 oz bag: 3-3/8" x 2-9/16" x 10-1/4"
Black 2 oz sample stand up pouch: 4" x 6-1/2" + 2-3/8", 2oz (60g)
Black 2lb bag: 5" x 3-3/8" x 15", 2lb (1kg)
Please include as much as possible below on the front label without it looking too wordy:
1) Our logo (it's attached). Feel free to do something creative with just the bean and place "Tidy-Pod" or "Tidy-Pod Coffees" somewhere else. They don't have to be together like in the attached file. The bean can be in the background of the label as well or something else cool like in the form of a cloud over the volcano or as the sun in the sky over the volcano.
2) lime green, burnt orange, dark brown & black
3) Front label should say:
"100% Premium Arabica Nicaraguan Coffee"
"Organic, Rain Forest & Mountain Shade Grown"
Bottom of label:
"Medium Roast"
"Full body, bold flavor, nutty, hints of chocolate, with a distinct & flavorful aroma."
I want one front label file for each size bag: "2 oz" "12 oz" & "32 oz"
Back of the label:
I have uploaded a hand drawn pic of what I am thinking but if you have a better idea please submit it.
Please include as much as possible below without it looking wordy:
Directions on the perfect cup:
***2 Tbsp high quality coffee 6 Oz. cup of pure filtered water
(these can be tied into the hand-drawn picture. I will label the section each one corresponds to)
Organically Grown (sustainable)
Rainforest Grown (sustainable)
Mountain Shade Grown (sustainable)
Hand Picked (select)
Spring Water Washed (select)
Sun Dried (select)
Social Responsibility (profits help fund Bright Path Outreach Nicaragua www.brightpathoutreach.example.org)
Single Source Coffee (Single source)
Traceable Source (single source)
Website: www.Tidy-Pod.example.com
Reason: I have been asked to extend deadline by a few designers.
Thanks,
Joanne Pelter
ages 18-54
- Should have a cool border. Maybe fade from one color to another or have something more original than just a 3x3 square border.

```html
<!DOCTYPE html>
<html lang="en">
<head>
<meta charset="utf-8">
<title>Tidy-Pod Coffee – Back Label</title>
<link rel="stylesheet" href="https://fonts.googleapis.com/css2?family=Arimo&family=Tinos:wght@700&display=swap">
<style>
  :root {
    --frame-gold: #f2c45e;
    --frame-orange: #d9862e;
    --frame-brown: #5a2f18;
    --ink-dark: #3f1a0e;
    --ink-text: #2a1a12;
    --accent-orange: #f07a1e;
    --brand-brown: #3b1a10;
    --arrow: #4a1f12;
  }
  * { box-sizing: border-box; margin: 0; padding: 0; }
  html, body {
    width: 1200px; height: 1200px; overflow: hidden;
    background: #ffffff;
  }
  .label {
    position: relative;
    width: 1200px; height: 1200px;
    background: linear-gradient(135deg, var(--frame-brown) 0%, var(--frame-orange) 45%, var(--frame-gold) 70%, var(--frame-orange) 100%);
  }
  .beans-photo {
    position: absolute; left: 20px; top: 20px; width: 1160px; height: 1160px;
    background:
      radial-gradient(ellipse 55% 35% at 85% 8%, rgba(244, 205, 115, 0.85), rgba(244, 205, 115, 0) 70%),
      radial-gradient(ellipse 60% 25% at 40% 95%, rgba(222, 196, 150, 0.9), rgba(222, 196, 150, 0) 70%),
      radial-gradient(ellipse 40% 30% at 10% 75%, rgba(214, 180, 128, 0.7), rgba(214, 180, 128, 0) 70%),
      linear-gradient(165deg, #9c7a58 0%, #b98a55 18%, #8a5632 40%, #6f4226 58%, #8d6140 74%, #c9a878 90%, #a98560 100%);
  }
  .directions {
    position: absolute; left: 72px; top: 62px;
    font-family: "Arimo", Arial, sans-serif;
    font-size: 38px; line-height: 58px;
    color: var(--ink-text);
    white-space: nowrap;
  }
  .pillar-title {
    position: absolute;
    font-family: "Tinos", "Times New Roman", serif;
    font-weight: 700;
    font-size: 54px; line-height: 64px;
    color: var(--ink-dark);
    white-space: nowrap;
  }
  .pillar-list {
    position: absolute;
    font-family: "Tinos", "Times New Roman", serif;
    font-weight: 700;
    font-size: 36px; line-height: 43px;
    color: var(--ink-dark);
    list-style: none;
    white-space: nowrap;
  }
  .single-source-title { left: 120px; top: 321px; }
  .single-source-list { left: 75px; top: 400px; }
  .sustainable-title { left: 774px; top: 321px; }
  .sustainable-list { right: 73px; top: 400px; text-align: right; }
  .select-title {
    left: 125px; top: 566px; width: 300px;
    text-align: center; color: var(--accent-orange);
    line-height: 59px;
  }
  .select-list { left: 75px; top: 749px; color: var(--accent-orange); }
  .social-title {
    left: 706px; top: 597px; width: 400px;
    text-align: center; line-height: 62px;
  }
  .social-list { right: 73px; top: 747px; text-align: right; }
  .brand-mark {
    position: absolute; left: 601px; top: 530px;
    transform: translate(-50%, -50%);
    display: flex; align-items: center; gap: 14px;
  }
  .brand-dot {
    width: 42px; height: 42px; border-radius: 50%;
    background: var(--brand-brown);
  }
  .brand-name {
    font-family: "Tinos", "Times New Roman", serif;
    font-weight: 700; font-size: 54px; line-height: 1;
    color: var(--brand-brown);
  }
  .cycle-arrows {
    position: absolute; left: 0; top: 0;
    width: 1200px; height: 1200px;
    pointer-events: none;
  }
  .footer-line {
    position: absolute; left: 0; width: 100%;
    text-align: center;
    font-family: "Arimo", Arial, sans-serif;
    font-size: 43px; line-height: 50px;
    color: var(--ink-text);
  }
  .tagline { top: 1002px; }
  .website { top: 1102px; }
</style>
</head>
<body>
<div class="label">
  <div class="beans-photo" role="img" aria-label="Photo of roasted coffee beans spilling from an open burlap sack"></div>

  <div class="directions">
    <p>Directions on the perfect cup:</p>
    <p>***2 Tbsp high quality coffee 6 Oz. cup of pure filtered water</p>
  </div>

  <h2 class="pillar-title single-source-title">Single Source</h2>
  <ul class="pillar-list single-source-list">
    <li>Single Source Coffee</li>
    <li>Traceable Source</li>
  </ul>

  <h2 class="pillar-title sustainable-title">Sustainable</h2>
  <ul class="pillar-list sustainable-list">
    <li>Organically Grown</li>
    <li>Rainforest Grown</li>
    <li>Mountain Shade Grown</li>
  </ul>

  <h2 class="pillar-title select-title">Select<br>Nicaraguan<br>Beans</h2>
  <ul class="pillar-list select-list">
    <li>Sun Dried</li>
    <li>Spring Water Washed</li>
    <li>Hand Picked</li>
  </ul>

  <h2 class="pillar-title social-title">Social<br>Responsibility</h2>
  <ul class="pillar-list social-list">
    <li>Profits help fund</li>
    <li>Bright Path Outreach Nicaragua</li>
    <li>www.brightpathoutreach.example.org</li>
  </ul>

  <svg class="cycle-arrows" viewBox="0 0 1200 1200" aria-hidden="true">
    <g fill="none" stroke="var(--arrow)" stroke-width="3" stroke-linecap="round" stroke-linejoin="round">
      <path d="M452 462 C440 432 462 412 500 414"/>
      <path d="M486 398 L504 414 L486 430"/>
      <path d="M672 412 C716 408 748 432 752 466"/>
      <path d="M736 452 L752 474 L768 452"/>
      <path d="M770 578 C778 612 752 636 712 642"/>
      <path d="M726 626 L706 642 L726 658"/>
      <path d="M524 648 C488 650 458 630 454 598"/>
      <path d="M438 612 L454 590 L470 612"/>
    </g>
  </svg>

  <div class="brand-mark">
    <span class="brand-dot"></span>
    <span class="brand-name">Tidy-Pod</span>
  </div>

  <p class="footer-line tagline">Growers with Social Responsibility</p>
  <p class="footer-line website">www.Tidy-Pod.example.com</p>
</div>
</body>
</html>
```